Design an Elegant Handbag Brand website

I need a webiste design are looking for ideas for a new theme, color scheme, etc. You come up with the general look and feel of the home page and our team will take it from there.
We're only looking for a one (1) page layout which should be fashionable and graphic intensive, but also include the standard homepage links (about us, see our collections, etc)

Target Market(s)

Our customers are fashionable women looking for an animal friendly and environmentally friendly handbag.

Industry/Entity Type

Business

Number of Pages Required

1 page

Font styles to use
Serif
Sans Serif

Requirements
Must have
• Feel free to modify it with different colors or tweaks as you see fit. We are open to all suggestions.
Nice to have

```html
<!DOCTYPE html>
<html lang="en">
<head>
<meta charset="utf-8">
<title>Verellan Fashions — Handbags</title>
<link href="https://fonts.googleapis.com/css2?family=Roboto:wght@400;500;700;900&family=Arimo:wght@400;700&display=swap" rel="stylesheet">
<style>
:root{
  --pink:#e8236c;
  --pink-deep:#c8104f;
  --ink:#1c1c1c;
  --text:#555;
  --muted:#888;
  --card:#f0f0f0;
  --star:#f29c1f;
  --footer:#1b1b1b;
  --white:#fff;
}
*{margin:0;padding:0;box-sizing:border-box}
html,body{width:1200px;height:3052px;overflow:hidden}
body{position:relative;background:var(--white);font-family:"Roboto",sans-serif;color:var(--ink)}
.abs{position:absolute}
.topline{left:0;top:0;width:1200px;height:5px;background:var(--pink)}

/* header */
.brand{left:112px;top:16px;display:flex;align-items:center;gap:10px}
.brand-mark{width:42px;height:42px;background:var(--pink);border-radius:4px}
.brand-name{font-weight:700;font-size:19px;line-height:24px;color:var(--ink);letter-spacing:.3px}
.nav{left:480px;top:43px;font-weight:500;font-size:16px}
.nav a{color:var(--ink);text-decoration:none;position:absolute;white-space:nowrap}
.nav a.active{color:var(--pink)}
.nav a.active::after{content:"";position:absolute;left:0;right:0;bottom:-8px;height:2px;background:var(--pink)}
.search{left:909px;top:45px}
.cart-btn{left:957px;top:33px;width:41px;height:41px;border-radius:50%;background:var(--pink);display:flex;align-items:center;justify-content:center}
.cart-label{left:1009px;top:37px;font-size:14px;font-weight:500;line-height:18px}
.cart-label span{display:block;font-size:13px;font-weight:400}
.cart-label b{color:var(--pink);font-weight:500}

/* hero */
.hero{left:0;top:104px;width:1200px;height:548px;background:linear-gradient(90deg,#6f5638 0%,#9a7c55 35%,#b89a72 60%,#a88661 80%,#8b6a47 100%)}
.hero-title{left:112px;top:276px;font-size:37px;font-weight:700;color:var(--white);letter-spacing:.5px}
.hero-text{left:113px;top:337px;width:520px;font-size:17px;font-weight:500;line-height:27px;color:var(--white)}
.btn{display:flex;align-items:center;gap:8px;background:var(--pink);color:var(--white);font-weight:700;border-radius:30px;justify-content:center}
.hero-btn{left:114px;top:420px;width:186px;height:52px;font-size:17px}
.arrow{width:36px;height:36px;border:2px solid var(--white);border-radius:50%;display:flex;align-items:center;justify-content:center}
.arrow-l{left:34px;top:359px}
.arrow-r{left:1126px;top:359px}

/* about */
.about-art{left:124px;top:746px;width:386px;height:378px}
.about-title{left:588px;top:780px;font-size:36px;font-weight:700;color:var(--ink)}
.about-title em{font-style:normal;color:var(--pink)}
.about-text{left:587px;top:847px;width:488px;font-family:"Arimo",sans-serif;font-size:16.5px;line-height:28.4px;color:var(--text);text-align:justify}

/* section titles */
.section-title{left:0;width:1200px;text-align:center;font-size:31px;font-weight:700;color:var(--ink)}

/* products */
.product{top:1310px;width:234px}
.product-img{width:234px;height:232px;background:var(--card);position:relative}
.product-img .shape{position:absolute;left:50px;top:40px;width:134px;height:150px;border-radius:12px;opacity:.85}
.tag{position:absolute;right:0;top:10px;background:var(--pink);color:var(--white);font-size:11px;padding:3px 5px}
.discount{position:absolute;left:6px;top:10px;width:43px;height:39px;background:var(--pink-deep);color:var(--white);font-weight:700;font-size:16px;text-align:center;line-height:16px;padding-top:4px}
.discount small{display:block;font-size:10px;font-weight:400}
.tool{position:absolute;left:11px;width:31px;height:27px;background:var(--pink);border-radius:3px;display:flex;align-items:center;justify-content:center}
.product-name{margin-top:26px;text-align:center;font-size:19px;font-weight:700}
.price{margin-top:6px;text-align:center;font-size:15px;font-weight:700}
.price s{color:var(--muted);margin-right:12px}
.price b{color:var(--pink-deep)}
.rating{margin-top:10px;text-align:center;font-size:12.5px;font-weight:500}
.rating i{font-style:normal;color:var(--star);letter-spacing:1px;margin-right:6px;font-size:13px}

/* deals */
.deals{left:0;top:1743px;width:1200px;height:425px;background:linear-gradient(90deg,#d97fa0 0%,#eaa3bd 45%,#f6c7d8 75%,#f1b3c9 100%)}
.deals-art{left:750px;top:1743px;width:300px;height:425px;background:linear-gradient(180deg,#efb1c6 0%,#4a8fd6 45%,#2f78c8 75%,#f0b9cc 100%);opacity:.55;border-radius:140px 140px 0 0}
.deals-title{left:201px;top:1846px;font-size:46px;font-weight:900;color:var(--white);letter-spacing:.5px}
.deals-text{left:203px;top:1917px;font-family:"Arimo",sans-serif;font-size:16.5px;line-height:26px;color:var(--white)}
.deals-btn{left:204px;top:2004px;width:162px;height:52px;font-size:16px}

/* testimonials */
.quote{top:2350px;width:311px;height:205px;border:1px solid #ddd;background:var(--white);text-align:center;padding:28px 12px 0}
.quote-mark{font-family:Georgia,serif;font-size:62px;font-weight:700;color:var(--pink);line-height:40px;height:44px}
.quote p{margin-top:8px;font-family:"Arimo",sans-serif;font-size:14.5px;line-height:25px;color:#555}
.quote::after{content:"";position:absolute;left:147px;bottom:-9px;width:16px;height:16px;background:var(--white);border-right:1px solid #ddd;border-bottom:1px solid #ddd;transform:rotate(45deg)}
.client{top:2580px;display:flex;align-items:center;gap:12px}
.avatar{width:48px;height:48px;border-radius:50%;background:linear-gradient(135deg,#8a5a3c,#c9946a)}
.client-name{font-size:16px;font-weight:500;line-height:20px}
.client-name span{display:block;font-size:13px;font-weight:400;color:var(--muted)}

/* footer */
.footer{left:0;top:2725px;width:1200px;height:327px;background:var(--footer);color:var(--white)}
.f-head{top:2786px;font-size:17px;font-weight:500;letter-spacing:.3px}
.f-list{top:2827px;list-style:none;font-size:14px;line-height:26.7px}
.f-rule{top:2790px;width:1px;height:170px;background:#2c2c2c}
.contact{top:2827px;font-size:14px}
.contact li{list-style:none;display:flex;gap:12px;align-items:flex-start;height:29px}
.contact svg{margin-top:3px;flex:none}
.contact u{text-decoration:underline}
.social{top:2832px;list-style:none;font-size:14px}
.social li{display:flex;align-items:center;gap:13px;height:33.5px}
.social .dot{width:29px;height:29px;border-radius:50%;background:var(--white)}
.copy{left:0;top:3008px;width:1200px;text-align:center;font-size:14px}
</style>
</head>
<body>
<div class="abs topline"></div>

<header>
  <div class="abs brand"><div class="brand-mark"></div><div class="brand-name">VERELLAN<br>FASHIONS</div></div>
  <nav class="abs nav">
    <a class="active" style="left:0">Home</a>
    <a style="left:73px">About</a>
    <a style="left:145px">Collections</a>
    <a style="left:253px">News</a>
    <a style="left:323px">Contact Us</a>
  </nav>
  <svg class="abs search" width="16" height="16" viewBox="0 0 16 16"><circle cx="6.5" cy="6.5" r="4.8" fill="none" stroke="#1c1c1c" stroke-width="2.2"/><line x1="10" y1="10" x2="14.5" y2="14.5" stroke="#1c1c1c" stroke-width="2.6" stroke-linecap="round"/></svg>
  <div class="abs cart-btn"><svg width="18" height="16" viewBox="0 0 18 16"><path d="M1 1h3l2 9h9l2-7H5" fill="none" stroke="#fff" stroke-width="2" stroke-linejoin="round"/><circle cx="7" cy="14" r="1.5" fill="#fff"/><circle cx="14" cy="14" r="1.5" fill="#fff"/></svg></div>
  <div class="abs cart-label">MY CART<span>0 item- <b>$0.00</b></span></div>
</header>

<section>
  <div class="abs hero" role="img" aria-label="Photo of a model in a tan jacket holding sunglasses and a leather handbag"></div>
  <h1 class="abs hero-title">VERELLAN FASHIONS</h1>
  <p class="abs hero-text">Sed ut perspiciatis unde omnis iste natus error sit voluptatem accusantium doloremque totam rem aperiam,</p>
  <div class="abs btn hero-btn">GET STARTED
    <svg width="16" height="16" viewBox="0 0 16 16"><circle cx="8" cy="8" r="7.5" fill="#fff"/><path d="M6 4.5 9.5 8 6 11.5" fill="none" stroke="#e8236c" stroke-width="2.2"/></svg></div>
  <div class="abs arrow arrow-l"><svg width="12" height="16" viewBox="0 0 12 16"><path d="M8 2 3 8l5 6" fill="none" stroke="#fff" stroke-width="2"/></svg></div>
  <div class="abs arrow arrow-r"><svg width="12" height="16" viewBox="0 0 12 16"><path d="m4 2 5 6-5 6" fill="none" stroke="#fff" stroke-width="2"/></svg></div>
</section>

<section>
  <svg class="abs about-art" viewBox="0 0 386 378" role="img" aria-label="Photo of a model holding a black leather handbag, framed in an organic shape">
    <path d="M60 40C120 -10 300 10 350 120C400 230 360 330 260 370C170 400 70 360 30 280C-10 200 0 90 60 40Z" fill="#e8236c"/>
    <path d="M75 55C140 5 280 5 340 95C390 180 380 300 290 345C200 385 60 360 15 270C-15 200 10 105 75 55Z" fill="#3a3a42"/>
  </svg>
  <h2 class="abs about-title"><em>ABOUT</em> US</h2>
  <p class="abs about-text">Lorem ipsum dolor sit amet, consectetur adipiscing elit, sed eiusmod tempor incididunt ut labore et dolore magna aliqua. Ut enim ad minim veniam, quis nostrud exercitation ullamco laboris nisi ut aliquip ex ea commodo consequat. Duis aute irure dolor in reprehenderit in voluptate velit esse cillum dolore eu fugiat nulla pariatur. Excepteur sint occaecat cupidatat non proident, sunt in culpa qui officia deserunt mollit anim id est laborum</p>
</section>

<section>
  <h2 class="abs section-title" style="top:1228px">FEATURED PRODUCTS</h2>

  <article class="abs product" style="left:112px">
    <div class="product-img" role="img" aria-label="Black leather tote bag">
      <div class="shape" style="background:#1d1d1d"></div>
      <span class="tag">FEATURED</span>
      <div class="tool" style="top:10px"><svg width="14" height="12" viewBox="0 0 18 16"><path d="M1 1h3l2 9h9l2-7H5" fill="none" stroke="#fff" stroke-width="2.4"/><circle cx="7" cy="14" r="1.6" fill="#fff"/><circle cx="14" cy="14" r="1.6" fill="#fff"/></svg></div>
      <div class="tool" style="top:41px"><svg width="14" height="12" viewBox="0 0 14 12"><path d="M7 11.5 1.5 6A3 3 0 0 1 7 2.5 3 3 0 0 1 12.5 6Z" fill="#fff"/></svg></div>
    </div>
    <div class="product-name">Product Name</div>
    <div class="price"><s>$95.00</s><b>$85.00</b></div>
    <div class="rating"><i>★★★★☆</i>50 Reviews</div>
  </article>

  <article class="abs product" style="left:360px">
    <div class="product-img" role="img" aria-label="Set of beige handbags with tassel"><div class="shape" style="background:#b89775"></div></div>
    <div class="product-name">Product Name</div>
    <div class="price"><s>$20.00</s><b>$10.80</b></div>
    <div class="rating"><i>★★★★☆</i>50 Reviews</div>
  </article>

  <article class="abs product" style="left:607px">
    <div class="product-img" role="img" aria-label="Navy blue structured tote bag"><div class="shape" style="background:#1f2a55"></div><span class="tag">FEATURED</span></div>
    <div class="product-name">Product Name</div>
    <div class="price"><s>$25.00</s><b>$20.00</b></div>
    <div class="rating"><i>★★★★☆</i>50 Reviews</div>
  </article>

  <article class="abs product" style="left:854px">
    <div class="product-img" role="img" aria-label="Black leather handbag with top handles"><div class="shape" style="background:#1a1a1a"></div><div class="discount">15%<small>OFF</small></div></div>
    <div class="product-name">Product Name</div>
    <div class="price"><s>$15.00</s><b>$10.95</b></div>
    <div class="rating"><i>★★★★☆</i>50 Reviews</div>
  </article>
</section>

<section>
  <div class="abs deals" role="img" aria-label="Pink backdrop with a model in a blue dress carrying a red quilted bag"></div>
  <div class="abs deals-art"></div>
  <h2 class="abs deals-title">DEALS OF THE DAY 15%</h2>
  <p class="abs deals-text">Lorem ipsum dolor sit amet, consectetur adipiscing elit,<br>sed do eiusmod tempor incididunt ut labore</p>
  <div class="abs btn deals-btn">SHOP NOW
    <svg width="15" height="15" viewBox="0 0 16 16"><circle cx="8" cy="8" r="7.5" fill="#fff"/><path d="M6 4.5 9.5 8 6 11.5" fill="none" stroke="#e8236c" stroke-width="2.2"/></svg></div>
</section>

<section>
  <h2 class="abs section-title" style="top:2264px">OUR CLIENTS LOVE US!</h2>

  <div class="abs quote" style="left:111px"><div class="quote-mark">“</div><p>This service gained me 10 listings for me over the past year! For me is the best and most powerful tool available in the Real Estate industry.</p></div>
  <div class="abs client" style="left:173px"><div class="avatar" role="img" aria-label="Client portrait"></div><div class="client-name">MARA LINDQVIST<span>USA</span></div></div>

  <div class="abs quote" style="left:444px"><div class="quote-mark">“</div><p>At Harborline Lending &amp; Cover, we have found CardLink to be an excellent tool for sharing our contact details. Simply asking them to txt ‘Noah to 555 014 220’</p></div>
  <div class="abs client" style="left:506px"><div class="avatar" role="img" aria-label="Client portrait"></div><div class="client-name">NOAH BRENNER<span>USA</span></div></div>

  <div class="abs quote" style="left:778px"><div class="quote-mark">“</div><p>The great thing I found with CardLink is people’s impressed reaction when they ask for a business card. Its also really handy if you run into someone</p></div>
  <div class="abs client" style="left:840px"><div class="avatar" role="img" aria-label="Client portrait"></div><div class="client-name">TESSA MARLOWE<span>USA</span></div></div>
</section>

<footer>
  <div class="abs footer"></div>
  <div class="abs f-rule" style="left:270px"></div>
  <div class="abs f-rule" style="left:536px"></div>
  <div class="abs f-rule" style="left:874px"></div>

  <h3 class="abs f-head" style="left:113px;color:#fff">QUICK LINKS</h3>
  <ul class="abs f-list" style="left:113px;color:#fff"><li>Home</li><li>About</li><li>Products</li><li>Reviews</li><li>Gallery</li></ul>

  <h3 class="abs f-head" style="left:349px;color:#fff">INFORMATION</h3>
  <ul class="abs f-list" style="left:349px;color:#fff"><li>Terms &amp; Conditions</li><li>Privacy Policy</li><li>Disclaimer</li><li>Site Map</li><li>Contact Us</li></ul>

  <h3 class="abs f-head" style="left:615px;color:#fff">CONTACT INFO</h3>
  <ul class="abs contact" style="left:615px;color:#fff">
    <li><svg width="14" height="12" viewBox="0 0 14 12"><path d="M1 4C1 1 13 1 13 4v1H10V3.5H4V5H1Z M3 6h8l1 5H2Z" fill="#fff"/></svg>(555) 014-2200</li>
    <li><svg width="14" height="12" viewBox="0 0 14 12"><rect x="3" y="0.5" width="8" height="4" fill="none" stroke="#fff"/><rect x="1" y="4" width="12" height="5" fill="#fff"/><rect x="3.5" y="8" width="7" height="3.5" fill="#fff" stroke="#1b1b1b"/></svg>(555) 014-220</li>
    <li><svg width="14" height="12" viewBox="0 0 14 12"><rect x="1" y="2" width="12" height="8" fill="#fff"/><path d="M1 2 7 7l6-5" fill="none" stroke="#1b1b1b"/></svg><u>hello@verellan.example</u></li>
    <li><svg width="14" height="14" viewBox="0 0 14 14"><path d="M7 13C3 8 3 6.5 3 5a4 4 0 0 1 8 0c0 1.5 0 3-4 8Z" fill="#fff"/><circle cx="7" cy="5" r="1.5" fill="#1b1b1b"/></svg><span style="line-height:15px">#2868 Lorem ipsum dolor<br>sit amet, consectetur</span></li>
  </ul>

  <h3 class="abs f-head" style="left:954px;color:#fff">FOLLOW US</h3>
  <ul class="abs social" style="left:954px;color:#fff">
    <li><span class="dot"></span>Friends Page</li>
    <li><span class="dot"></span>Short Posts</li>
    <li><span class="dot"></span>Circles</li>
    <li><span class="dot"></span>Work Network</li>
  </ul>

  <p class="abs copy" style="color:#fff">Copyrights © The Company name 2020 | Allrights Reserved</p>
</footer>
</body>
</html>
```